Award Winning Patient Support Program needs infographics designed

I need two infographics created for my website and my pitch decks. I have two services I offer. Each service has 6 elements to it. I developed and launched an innovative, coaching-based program to help patients better manage side effects and stress as a solution to a challenge that costs healthcare $600 billion annually and costs patients quality of life and reduces positive outcomes. One of the services, my Patient Adherence Training Program, trains healthcare professionals such as pharmacists, nurses, and doctors, to use coaching skills and a behavior change strategy I designed to help them better listen to, understand, and support patients. The program includes live training intensives, coaching skills development webinars, a customized coaching guide, video training and support documents library, side effect management plan, and confidential patient call review. The second program is my Patient Support Program - it provides patients texting/email support programs, peer mentor support, online group coaching program, side effect management plan, caregiver support, and stress reduction strategies. The program was one of 9 finalists for the 2018 Velmora T9 Pioneering Patient Support Prize and I was invited to resubmit again this year. The goal of the infographics is to visually illustrate the 6 core elements of the two programs. Adherence and behavior change require comprehensive solutions - therefore the programs have to be robust - but I need to simplify the introduction to what each program includes. Patients deserve better support and are often judged as being lazy when they stop taking medication or don't follow "doctor's orders" - when, in fact, it is a complex list of factors that cause non-adherence. My programs also give them skills to help them enjoy better quality of life. The infographic design I envisioned and mocked up uses icons and can include text naming each icon for clarity. I don't expect the infographic to rely on the image of each icon alone. Also, there is one program element that is the same for both - the side effect management plan - so, while there are 12 elements between the two programs, there will be 11 icons. I would need each of the 11 icons in separate files as well as in a file with the finished infographic so I can use the icons independent of the infographic when I go into detailed slides/breakdown of the elements. I have attached a mock up with notes and breaking out the icons. I have also attached the wireframe for the new landing page to show how the infographics will be featured on the web page. My Bright Lantern Path logo was designed using Pixgrove and I still love it and get compliments all the time so I'm turning to this process again and hoping for as great an experience and outcome!

Target Market(s)

Healthcare organizations and pharmaceutical companies

Industry/Entity Type

Pharmaceutical

Font styles to use
Sans Serif

Colors
0792cd
f37122
ffffff

Requirements
Must have
• Consistent design for each icon in the infographic, readable text description of each icon, originally created icons - please do not use the samples in the brief as they are just to give an idea - I do not own the copyright to them.
Should not have
• Don't be insensitive to gender/culture/diversity in choice of icons - needs to be non-specific or a diverse representation

```html
<!DOCTYPE html>
<html lang="en">
<head>
<meta charset="utf-8">
<title>Organizational Training &amp; Resources</title>
<link rel="stylesheet" href="https://fonts.googleapis.com/css2?family=Fjalla+One&family=Oswald:wght@300;500&family=Open+Sans:wght@400;700&display=swap">
<style>
  :root {
    --teal: #1d9fb6;
    --navy: #1f3a7f;
    --band: #233d7e;
    --ink: #333333;
    --body: #3a3a3a;
    --white: #ffffff;
  }
  html, body { margin: 0; padding: 0; overflow: hidden; }
  .canvas {
    position: relative;
    width: 1200px;
    height: 1200px;
    background: var(--white);
    overflow: hidden;
    font-family: "Open Sans", Arial, sans-serif;
  }
  .hero-illustration {
    position: absolute;
    left: 132px; top: 32px;
    width: 336px; height: 244px;
    border-radius: 18px;
    background: linear-gradient(135deg, #e6f4f7 0%, #cfe9ef 55%, #f7e2c8 100%);
  }
  .title-rule {
    position: absolute;
    left: 465px; top: 132px;
    width: 1px; height: 100px;
    background: var(--navy);
  }
  .title {
    position: absolute;
    left: 500px; top: 56px;
    margin: 0;
    font-family: "Fjalla One", "Oswald", sans-serif;
    font-weight: 400;
    font-size: 82px;
    line-height: 96px;
    color: var(--teal);
    letter-spacing: 0.5px;
  }
  .program-label {
    position: absolute;
    right: 802px; top: 298px;
    margin: 0;
    text-align: right;
    font-family: "Oswald", sans-serif;
    font-weight: 300;
    font-size: 27px;
    line-height: 36px;
    color: var(--ink);
    text-transform: uppercase;
  }
  .intro {
    position: absolute;
    left: 502px; top: 294px;
    margin: 0;
    font-family: "Fjalla One", "Oswald", sans-serif;
    font-size: 33px;
    line-height: 46px;
    color: var(--ink);
  }
  .intro .count { color: var(--navy); }
  .component {
    position: absolute;
    width: 430px;
  }
  .component .ring {
    position: absolute;
    left: 0; top: 0;
    width: 190px; height: 190px;
    border-radius: 50%;
  }
  .component .ring::after {
    content: "";
    position: absolute;
    left: 20px; top: 20px;
    width: 150px; height: 150px;
    border-radius: 50%;
    background: var(--white);
    box-shadow: 4px 6px 10px rgba(0,0,0,0.18);
  }
  .component .icon-art {
    position: absolute;
    left: 45px; top: 45px;
    width: 100px; height: 100px;
    border-radius: 50%;
    z-index: 1;
  }
  .component .text {
    position: absolute;
    left: 212px;
    width: 270px;
  }
  .component h3 {
    margin: 0 0 8px;
    font-family: "Open Sans", Arial, sans-serif;
    font-weight: 700;
    font-size: 30px;
    line-height: 38px;
    color: var(--navy);
    letter-spacing: 0.3px;
  }
  .component h3 .sub { display: block; font-size: 24px; line-height: 30px; }
  .component p {
    margin: 0;
    font-size: 12px;
    line-height: 15.4px;
    color: var(--body);
    width: 256px;
  }
  .ring-orange { background: linear-gradient(135deg, #f7931e, #fbb23f 60%, #fcc659); }
  .ring-purple { background: linear-gradient(135deg, #4d3f95, #7c64b5 55%, #b29bd8); }
  .ring-crimson { background: linear-gradient(135deg, #b8123f, #d72c57 55%, #e6577a); }
  .ring-blue { background: linear-gradient(135deg, #1a5fb5, #2a8fd6 55%, #55bfea); }
  .ring-green { background: linear-gradient(135deg, #279c8a, #6cc19a 55%, #b4dd8e); }
  .ring-grey { background: linear-gradient(135deg, #2b2b2b, #5e5e5e 55%, #a8a8a8); }
  .art-orange { background: linear-gradient(135deg, #fdeed6, #f9d3a0); }
  .art-purple { background: linear-gradient(135deg, #dfe7f3, #2c4a6e); }
  .art-crimson { background: linear-gradient(135deg, #e7f2f6, #1f3f6e); }
  .art-blue { background: linear-gradient(135deg, #cdeef4, #f5c221); }
  .art-green { background: linear-gradient(135deg, #fbd16a, #ee6a22); }
  .art-grey { background: linear-gradient(135deg, #dcebf3, #ef7d1e); }
  .footer-band {
    position: absolute;
    left: 0; top: 1122px;
    width: 1200px; height: 78px;
    background: var(--band);
  }
</style>
</head>
<body>
<main class="canvas">
  <div class="hero-illustration" role="img" aria-label="Illustration of healthcare professionals with a clipboard and a large medical chart with gears and graphs"></div>
  <div class="title-rule"></div>
  <h1 class="title">Organizational<br>Training &amp; Resources</h1>
  <p class="program-label">The program for<br>training healthcare and<br>pharma organizations</p>
  <h2 class="intro"><span class="count">6 core components</span><br>of the Patient Adherence Training Program</h2>

  <section class="component" style="left:114px; top:427px;">
    <div class="ring ring-orange"></div>
    <div class="icon-art art-orange" role="img" aria-label="Icon of a trainer presenting at a flip chart"></div>
    <div class="text" style="top:16px;">
      <h3>Live Training<br>Intensives</h3>
      <p>Coaching-based program to help patients better manage side effects and stress as a solution to a challenge that costs healthcare $600 billion annually and costs patients quality of life and reduces positive outcomes.</p>
    </div>
  </section>

  <section class="component" style="left:607px; top:423px;">
    <div class="ring ring-purple"></div>
    <div class="icon-art art-purple" role="img" aria-label="Icon of a clipboard with a plan checklist"></div>
    <div class="text" style="top:17px;">
      <h3>Side Effect<br>Management Plan</h3>
      <p>Coaching-based program to help patients better manage side effects and stress as a solution to a challenge that costs healthcare $600 billion annually and costs patients quality of life and reduces positive outcomes.</p>
    </div>
  </section>

  <section class="component" style="left:114px; top:635px;">
    <div class="ring ring-crimson"></div>
    <div class="icon-art art-crimson" role="img" aria-label="Icon of a laptop with two headset-wearing webinar participants"></div>
    <div class="text" style="top:9px;">
      <h3>Coaching Skills<span class="sub">Development Webinars</span></h3>
      <p style="margin-top:10px;">Coaching-based program to help patients better manage side effects and stress as a solution to a challenge that costs healthcare $600 billion annually and costs patients quality of life and reduces positive outcomes.</p>
    </div>
  </section>

  <section class="component" style="left:607px; top:635px;">
    <div class="ring ring-blue"></div>
    <div class="icon-art art-blue" role="img" aria-label="Icon of a hand tapping play on a tablet video"></div>
    <div class="text" style="top:4px;">
      <h3>Video Training<br>Library</h3>
      <p>Coaching-based program to help patients better manage side effects and stress as a solution to a challenge that costs healthcare $600 billion annually and costs patients quality of life and reduces positive outcomes.</p>
    </div>
  </section>

  <section class="component" style="left:114px; top:849px;">
    <div class="ring ring-green"></div>
    <div class="icon-art art-green" role="img" aria-label="Icon of an orange coaching guide booklet"></div>
    <div class="text" style="top:16px;">
      <h3>Customized<br>Coaching Guide</h3>
      <p>Coaching-based program to help patients better manage side effects and stress as a solution to a challenge that costs healthcare $600 billion annually and costs patients quality of life and reduces positive outcomes.</p>
    </div>
  </section>

  <section class="component" style="left:607px; top:851px;">
    <div class="ring ring-grey"></div>
    <div class="icon-art art-grey" role="img" aria-label="Icon of a call agent with headset and speech bubbles"></div>
    <div class="text" style="top:16px;">
      <h3>Confidential<br>Patient Call Review</h3>
      <p>Coaching-based program to help patients better manage side effects and stress as a solution to a challenge that costs healthcare $600 billion annually and costs patients quality of life and reduces positive outcomes.</p>
    </div>
  </section>

  <div class="footer-band"></div>
</main>
</body>
</html>
```